Tolvane Air and Electrical Website

Simple and easy to use website for a Electrical and Air Conditioning contracting business.Use stock photosOnline contact portallogo still to be supplied

Target Market(s)

Mums and Dads who want a local contractor

Coding

Coded - Design and coding required

Number of Pages Required

2 page

Font styles to use
Sans Serif

Colors
f04a50
3276b5
33a6d7

Requirements
Must have
• Simple and easy to use
• Ph number
• 4 web address; linked to page
• 0417385926
• tolvane.com.au
• tolvaneelectrical.com.au
• tolvaneairandelectrical.com.au
• tolvaneair.com.au
Nice to have
• Split System Air Con Picture
• Electrical Pictures

```html
<!DOCTYPE html>
<html lang="en">
<head>
<meta charset="utf-8">
<title>Tolvane Air and Electrical</title>
<link rel="stylesheet" href="https://fonts.googleapis.com/css2?family=Exo+2:wght@500;600;700;800&family=Roboto:wght@400;500;700&display=swap">
<style>
:root{
  --red:#f04a50;
  --blue:#3276b5;
  --sky:#33a6d7;
  --navy:#1f5a91;
  --ink:#333b45;
  --muted:#7a8490;
  --line:#e3e7ec;
  --white:#ffffff;
  --soft:#f5f7fa;
}
*{margin:0;padding:0;box-sizing:border-box}
html,body{width:1200px;height:3080px;overflow:hidden}
body{font-family:'Roboto',sans-serif;color:var(--ink);background:var(--white);position:relative}
.heading{font-family:'Exo 2',sans-serif}
section,header,footer{position:absolute;left:0;width:1200px}

/* header */
.site-header{top:0;height:190px;background:var(--white)}
.brand{position:absolute;left:80px;top:26px;display:flex;align-items:center;gap:12px}
.brand-square{width:40px;height:40px;background:var(--blue)}
.brand-name{font-family:'Exo 2',sans-serif;font-weight:800;font-size:30px;color:var(--blue);letter-spacing:.5px;line-height:1}
.contact-strip{position:absolute;top:20px;right:70px;display:flex;gap:40px}
.contact-item{display:flex;align-items:center;gap:12px}
.contact-item svg{width:30px;height:30px}
.contact-item small{display:block;font-size:13px;color:var(--muted)}
.contact-item b{display:block;font-size:16px;font-weight:500;color:var(--ink)}
.main-nav{position:absolute;top:112px;left:80px;right:80px;height:64px;border-top:1px solid var(--line);border-bottom:1px solid var(--line);display:flex;align-items:center}
.main-nav a{font-size:14px;color:var(--ink);text-decoration:none;text-transform:uppercase;margin-right:44px;letter-spacing:.5px}
.main-nav a.current{border:1px solid var(--blue);color:var(--blue);padding:10px 18px;margin-right:40px}
.btn-red{background:var(--red);color:var(--white);font-weight:500;font-size:16px;border-radius:4px;padding:15px 26px;text-decoration:none;display:inline-block}
.main-nav .btn-red{position:absolute;right:0;margin:0;text-transform:none;font-size:16px;color:var(--white);letter-spacing:0}

/* hero */
.hero{top:190px;height:620px}
.hero-photo{position:absolute;inset:0;background:linear-gradient(180deg,#f3f2ef 0%,#e9e6e1 55%,#d7d4cf 100%)}
.hero-copy{position:absolute;top:145px;left:0;right:0;text-align:center}
.hero-copy h1{font-family:'Exo 2',sans-serif;font-weight:700;font-size:48px;color:var(--blue);letter-spacing:1px}
.hero-copy p{width:640px;margin:14px auto 0;font-size:16px;line-height:1.5;color:var(--ink)}
.slide-arrow{position:absolute;top:285px;width:54px;height:54px;border-radius:50%;background:var(--white);box-shadow:0 2px 8px rgba(0,0,0,.15)}
.slide-arrow svg{width:54px;height:54px}
.slide-arrow.prev{left:28px}
.slide-arrow.next{right:28px}

/* services */
.services{top:810px;height:270px;background:var(--white);border-bottom:1px solid var(--line)}
.services-track{position:absolute;left:110px;right:110px;top:60px;display:flex;justify-content:space-between}
.service{width:180px;text-align:center}
.service-icon{width:100px;height:100px;margin:0 auto;border-radius:8px;background:var(--white);box-shadow:0 3px 12px rgba(0,0,0,.12);display:flex;align-items:center;justify-content:center}
.service-icon svg{width:56px;height:56px}
.service.active .service-icon{background:var(--sky)}
.service p{margin-top:20px;font-size:15px;line-height:1.35;color:var(--ink)}
.track-arrow{position:absolute;top:108px;width:30px;height:50px}
.track-arrow.prev{left:50px}
.track-arrow.next{right:50px}

/* repairs */
.repairs{top:1080px;height:400px;background:var(--white)}
.technician{position:absolute;left:200px;top:30px;width:300px;height:370px;background:linear-gradient(180deg,#e7ecf2,#2f5f9e 55%,#23497a)}
.repairs-copy{position:absolute;left:580px;top:70px;width:480px;text-align:center}
.repairs-copy .kicker{font-family:'Exo 2',sans-serif;color:var(--red);font-size:19px;font-weight:600}
.repairs-copy h2{font-family:'Exo 2',sans-serif;color:var(--blue);font-size:40px;font-weight:700;margin-top:4px}
.repairs-copy p{margin-top:18px;font-size:14px;line-height:1.6;color:var(--muted)}
.repairs-actions{margin-top:30px;display:flex;align-items:center;justify-content:center;gap:30px}
.phone-link{display:flex;align-items:center;gap:10px;font-size:24px;color:var(--blue)}
.phone-link svg{width:26px;height:26px}

/* quality & price */
.values{top:1480px;height:420px;display:flex}
.value{width:600px;height:420px;padding:60px 70px 0;color:var(--white)}
.value.quality{background:var(--sky)}
.value.price{background:var(--blue);padding-left:130px}
.value svg{width:78px;height:78px}
.value h3{font-family:'Exo 2',sans-serif;font-size:44px;font-weight:700;margin-top:18px}
.value p{font-size:14px;line-height:1.6;margin-top:12px;width:400px}
.value-badge{position:absolute;left:540px;top:150px;width:120px;height:120px;border-radius:50%;background:var(--white);border:6px solid var(--sky)}

/* feedback */
.feedback{top:1900px;height:660px;background:var(--white)}
.feedback h2{font-family:'Exo 2',sans-serif;text-align:center;color:var(--blue);font-size:44px;font-weight:700;margin-top:50px}
.feedback-card{position:absolute;left:240px;top:190px;width:720px;height:330px;background:var(--white);box-shadow:0 2px 14px rgba(0,0,0,.12);text-align:center;padding:120px 60px 0}
.avatar{position:absolute;left:300px;top:-60px;width:120px;height:120px;border-radius:50%;border:5px solid var(--white);box-shadow:0 0 0 3px var(--red);background:linear-gradient(135deg,#e8cfc0,#b78d78)}
.feedback-card p{font-size:14px;line-height:1.7;color:var(--muted)}
.quote-mark{font-family:'Exo 2',sans-serif;font-size:80px;line-height:.7;color:var(--red);margin-top:26px;height:44px;font-weight:800}
.reviewer{color:var(--red);font-size:16px;font-weight:500;margin-top:12px}
.reviewer-note{font-size:12px;color:var(--muted);margin-top:8px}
.dots{position:absolute;left:0;right:0;top:570px;display:flex;justify-content:center;gap:10px}
.dots span{width:14px;height:14px;border-radius:50%;border:2px solid var(--red)}
.dots span.on{background:var(--red)}

/* footer */
.site-footer{top:2560px;height:520px;background:var(--blue);color:var(--white)}
.footer-cols{position:absolute;left:80px;right:80px;top:60px;display:flex;justify-content:space-between}
.footer-col{width:320px}
.footer-col h4{font-family:'Exo 2',sans-serif;font-size:22px;font-weight:600;margin-bottom:22px}
.footer-col p{font-size:14px;line-height:1.6}
.footer-col p b{font-weight:700}
.site-links{margin-top:26px;list-style:none}
.site-links li{display:flex;align-items:center;gap:10px;font-size:13px;margin-bottom:14px}
.site-links li::before{content:"";width:14px;height:14px;border-radius:50%;background:rgba(255,255,255,.85)}
.post{display:flex;gap:16px;margin-bottom:20px}
.post-thumb{width:64px;height:64px;border-radius:50%;background:linear-gradient(135deg,#cfd8e2,#8fa6bd);flex:none}
.post b{display:block;font-size:14px;font-weight:500;line-height:1.4}
.post small{font-size:12px;opacity:.85}
.contact-list li{display:flex;gap:14px;font-size:14px;line-height:1.5;margin-bottom:16px;list-style:none}
.contact-list svg{width:20px;height:20px;flex:none;margin-top:1px}
.directions{margin-top:8px;width:300px;height:44px;border-radius:22px;background:rgba(255,255,255,.2);display:flex;align-items:center;justify-content:space-between;padding:0 20px;font-size:13px}
.socials{display:flex;gap:12px;margin-top:22px}
.socials span{width:40px;height:40px;border-radius:50%;background:var(--navy)}
.copyright{position:absolute;left:0;right:0;bottom:0;height:44px;background:var(--navy);text-align:center;font-size:13px;line-height:44px}
.copyright b{font-weight:700}
</style>
</head>
<body>

<header class="site-header">
  <div class="brand"><span class="brand-square"></span><span class="brand-name">Tolvane Air and Electrical</span></div>
  <div class="contact-strip">
    <div class="contact-item">
      <svg viewBox="0 0 24 24" fill="none" stroke="#3276b5" stroke-width="1.8"><path d="M5 3h4l2 5-3 2a12 12 0 0 0 6 6l2-3 5 2v4a2 2 0 0 1-2 2A17 17 0 0 1 3 5a2 2 0 0 1 2-2z"/></svg>
      <div><small>Call Us Now</small><b>0417385926</b></div>
    </div>
    <div class="contact-item">
      <svg viewBox="0 0 24 24" fill="none" stroke="#3276b5" stroke-width="1.8"><circle cx="12" cy="12" r="9"/><path d="M12 7v5l3 2"/></svg>
      <div><small>Work time</small><b>8:00 - 18:00</b></div>
    </div>
    <div class="contact-item">
      <svg viewBox="0 0 24 24" fill="none" stroke="#3276b5" stroke-width="1.8"><path d="M12 22s7-7 7-12a7 7 0 0 0-14 0c0 5 7 12 7 12z"/><circle cx="12" cy="10" r="2.5"/></svg>
      <div><small>123, Brisbane</small><b>Australia,1234</b></div>
    </div>
  </div>
  <nav class="main-nav">
    <a class="current" href="#">Home</a>
    <a href="#">About</a>
    <a href="#">Why Us</a>
    <a href="#">Quality</a>
    <a href="#">Price</a>
    <a href="#">Services</a>
    <a href="#">Contact</a>
    <a class="btn-red" href="#">Make an Appointment</a>
  </nav>
</header>

<section class="hero">
  <div class="hero-photo" role="img" aria-label="Stock photo of a family relaxing on a sofa in a bright living room with a split system air conditioner on the wall"></div>
  <div class="hero-copy">
    <h1>TOLVANE AIR AND ELECTRICAL</h1>
    <p>Lorem ipsum dolor sit amet, consectetur adipiscing elit, sed do eiusmod tempor incididunt ut labore et dolore magna aliqua. Ut enim ad minim veniam.</p>
  </div>
  <span class="slide-arrow prev"><svg viewBox="0 0 54 54"><path d="M30 19l-8 8 8 8" fill="none" stroke="#333b45" stroke-width="2.5"/></svg></span>
  <span class="slide-arrow next"><svg viewBox="0 0 54 54"><path d="M24 19l8 8-8 8" fill="none" stroke="#333b45" stroke-width="2.5"/></svg></span>
</section>

<section class="services">
  <svg class="track-arrow prev" viewBox="0 0 30 50"><path d="M22 6L8 25l14 19" fill="none" stroke="#7a8490" stroke-width="2.5"/></svg>
  <div class="services-track">
    <div class="service">
      <div class="service-icon"><svg viewBox="0 0 56 56" fill="none" stroke="#f04a50" stroke-width="2.2"><rect x="6" y="14" width="44" height="18" rx="3"/><path d="M10 26h36M18 38v8M28 38v10M38 38v8"/></svg></div>
      <p>Split System<br>Installations</p>
    </div>
    <div class="service">
      <div class="service-icon"><svg viewBox="0 0 56 56" fill="none" stroke="#f04a50" stroke-width="2.2"><path d="M8 28L28 10l20 18M14 24v22h28V24"/><path d="M30 26l-6 8h8l-6 8"/></svg></div>
      <p>Data &amp; Communication<br>Installation</p>
    </div>
    <div class="service active">
      <div class="service-icon"><svg viewBox="0 0 56 56" fill="none" stroke="#ffffff" stroke-width="2.2"><path d="M8 48V22l12 8v-8l12 8V10h8v38zM4 48h48"/><path d="M14 38h4M24 38h4M34 38h4"/></svg></div>
      <p>Industrial</p>
    </div>
    <div class="service">
      <div class="service-icon"><svg viewBox="0 0 56 56" fill="none" stroke="#f04a50" stroke-width="2.2"><rect x="16" y="18" width="24" height="20" rx="4"/><path d="M22 10v8M34 10v8M28 38v12"/></svg></div>
      <p>Electrical Testing &amp;<br>Tagging</p>
    </div>
    <div class="service">
      <div class="service-icon"><svg viewBox="0 0 56 56" fill="none" stroke="#f04a50" stroke-width="2.2"><path d="M14 42l18-18M32 24a8 8 0 1 0 10-10l-5 5-4-1-1-4 5-5a8 8 0 0 0-10 10"/><path d="M12 14l8 8M10 16l4-4"/></svg></div>
      <p>24 hr Breakdown &amp;<br>Repair Service</p>
    </div>
  </div>
  <svg class="track-arrow next" viewBox="0 0 30 50"><path d="M8 6l14 19L8 44" fill="none" stroke="#7a8490" stroke-width="2.5"/></svg>
</section>

<section class="repairs">
  <div class="technician" role="img" aria-label="Stock photo of a smiling electrician in blue overalls holding a tool bag"></div>
  <div class="repairs-copy">
    <div class="kicker">A Electrical and Air Conditioning</div>
    <h2>Repairs &amp; Services</h2>
    <p>With over 17 years' experience in the Electrical Industry, Tolvane Electrical provides a superior level of knowledge, a broad range of products and a high standard of customer service.</p>
    <div class="repairs-actions">
      <a class="btn-red" href="#">Make an Appointment</a>
      <span class="phone-link"><svg viewBox="0 0 24 24" fill="none" stroke="#3276b5" stroke-width="1.8"><path d="M5 3h4l2 5-3 2a12 12 0 0 0 6 6l2-3 5 2v4a2 2 0 0 1-2 2A17 17 0 0 1 3 5a2 2 0 0 1 2-2z"/></svg>0417385926</span>
    </div>
  </div>
</section>

<section class="values">
  <div class="value quality">
    <svg viewBox="0 0 78 78" fill="none" stroke="#ffffff" stroke-width="2.2"><circle cx="39" cy="30" r="18"/><circle cx="39" cy="30" r="11"/><path d="M27 44l-8 24 10-5 6 9 4-20M51 44l8 24-10-5-6 9-4-20"/></svg>
    <h3>Quality</h3>
    <p>We are committed to best practice electrical safety standards and highest quality performance on the job. Our team of qualified and experienced electricians provide personalised service based on professionalism and integrity. We aim to build long term business relationships and offer information and advice when you need it.</p>
  </div>
  <div class="value price">
    <svg viewBox="0 0 78 78" fill="none" stroke="#ffffff" stroke-width="2.2"><rect x="16" y="8" width="46" height="62" rx="4"/><rect x="23" y="15" width="32" height="14"/><path d="M25 40h6M36 40h6M47 40h6M25 50h6M36 50h6M47 50h6M25 60h6M36 60h6M47 60h6"/></svg>
    <h3>Price</h3>
    <p>Price is always important and our standard rates are competitive. Where jobs require an individual approach, we provide a comprehensive quote. Work is completed according to the quote at the agreed price.</p>
  </div>
  <span class="value-badge"></span>
</section>

<section class="feedback">
  <h2>Clients Feedback</h2>
  <div class="feedback-card">
    <div class="avatar" role="img" aria-label="Portrait photo of the reviewing client"></div>
    <p>Excellent service. Travis came out quickly at the agreed time. The team cleaned up after themselves and explained everything along the way. Friendly, tidy and professional and I would highly recommend them. I will surely use them for any future work.</p>
    <div class="quote-mark">&#8221;</div>
    <div class="reviewer">- Kate from Oakleigh, VIC</div>
    <div class="reviewer-note">Split System Air Conditioning Installation</div>
  </div>
  <div class="dots"><span class="on"></span><span></span><span></span></div>
</section>

<footer class="site-footer">
  <div class="footer-cols">
    <div class="footer-col">
      <h4>Our company</h4>
      <p>With over 17 years' experience in the Electrical Industry, Tolvane Electrical provides a superior level of knowledge, a broad range of products and a high... <b>READ MORE</b></p>
      <ul class="site-links">
        <li>tolvane.com.au</li>
        <li>tolvaneelectrical.com.au</li>
        <li>tolvaneairandelectrical.com.au</li>
        <li>tolvaneair.com.au</li>
      </ul>
    </div>
    <div class="footer-col">
      <h4>Recent Blog</h4>
      <div class="post"><span class="post-thumb" role="img" aria-label="Blog post thumbnail photo"></span><div><b>Lorem ipsum dolor sit amet, consectetur.</b><small>1 June 2019</small></div></div>
      <div class="post"><span class="post-thumb" role="img" aria-label="Blog post thumbnail photo"></span><div><b>Lorem ipsum dolor sit amet, consectetur.</b><small>1 June 2019</small></div></div>
      <div class="post"><span class="post-thumb" role="img" aria-label="Blog post thumbnail photo"></span><div><b>Lorem ipsum dolor sit amet, consectetur.</b><small>1 June 2019</small></div></div>
    </div>
    <div class="footer-col">
      <h4>Contact Corner</h4>
      <ul class="contact-list">
        <li><svg viewBox="0 0 24 24" fill="none" stroke="#ffffff" stroke-width="1.8"><path d="M5 3h4l2 5-3 2a12 12 0 0 0 6 6l2-3 5 2v4a2 2 0 0 1-2 2A17 17 0 0 1 3 5a2 2 0 0 1 2-2z"/></svg>0417385926</li>
        <li><svg viewBox="0 0 24 24" fill="none" stroke="#ffffff" stroke-width="1.8"><rect x="3" y="5" width="18" height="14" rx="2"/><path d="M3 7l9 6 9-6"/></svg>info@tolvane.com</li>
        <li><svg viewBox="0 0 24 24" fill="none" stroke="#ffffff" stroke-width="1.8"><path d="M12 22s7-7 7-12a7 7 0 0 0-14 0c0 5 7 12 7 12z"/><circle cx="12" cy="10" r="2.5"/></svg>123, Address, State Name,<br>City Name, Zipcode</li>
      </ul>
      <div class="directions"><span>Get directions on the map</span><svg width="22" height="12" viewBox="0 0 22 12"><path d="M0 6h20M15 1l5 5-5 5" fill="none" stroke="#ffffff" stroke-width="1.8"/></svg></div>
      <div class="socials"><span></span><span></span><span></span><span></span></div>
    </div>
  </div>
  <div class="copyright">Copyright © <b>TOLVANE AIR AND ELECTRICAL</b> 2019 - All Rights Reserved</div>
</footer>

</body>
</html>
```